Business card design for engineering firm specializing in defense industry.

We need a professional business card design. Something simple but stands out. We are an engineering company specializing in composites in the defense industry.
Industry/Entity Type
Defense
Contact Information for Business Card
A simple black business card with the Varlonix yellow color is what we had in mind but open for other designs.
Colors
ffc214

```html
<!DOCTYPE html>
<html lang="en">
<head>
<meta charset="utf-8">
<title>Varlonix Business Card</title>
<link href="https://fonts.googleapis.com/css2?family=Lato:wght@400;700;900&display=swap" rel="stylesheet">
<style>
  :root {
    --stage: #222222;
    --brand-yellow: #ffc214;
    --ink: #111111;
    --paper: #ffffff;
    --shadow: rgba(0, 0, 0, 0.55);
  }
  * { margin: 0; padding: 0; box-sizing: border-box; }
  html, body {
    width: 1200px;
    height: 900px;
    overflow: hidden;
    background: var(--stage);
    font-family: "Lato", Arial, sans-serif;
  }
  .stage {
    position: relative;
    width: 1200px;
    height: 900px;
  }
  .card {
    position: absolute;
    top: 200px;
    width: 310px;
    height: 502px;
    box-shadow: 3px 4px 6px var(--shadow);
  }
  .card--front {
    left: 253px;
    background: var(--paper);
    border-radius: 64px 0 64px 0;
  }
  .card--back {
    left: 627px;
    background: var(--brand-yellow);
    border-radius: 0 70px 0 70px;
  }
  .wordmark {
    position: absolute;
    left: 0;
    width: 100%;
    text-align: center;
    font-weight: 900;
    color: var(--ink);
    letter-spacing: 0.5px;
  }
  .card--front .wordmark {
    top: 132px;
    font-size: 42px;
  }
  .card--back .wordmark {
    top: 224px;
    font-size: 46px;
  }
  .contact {
    position: absolute;
    left: 24px;
    top: 302px;
    color: var(--ink);
  }
  .contact__name {
    color: var(--brand-yellow);
    font-size: 18px;
    font-weight: 400;
    letter-spacing: 0.2px;
    line-height: 22px;
  }
  .contact__title {
    font-size: 14px;
    line-height: 18px;
    margin-left: 1px;
  }
  .contact__company {
    margin-top: 9px;
    font-size: 14px;
    font-weight: 700;
    line-height: 18px;
    letter-spacing: 0.2px;
  }
  .contact__address {
    font-size: 14px;
    line-height: 18px;
  }
  .contact__lines {
    list-style: none;
    margin-top: 8px;
  }
  .contact__lines li {
    display: flex;
    align-items: center;
    font-size: 14px;
    line-height: 18.5px;
  }
  .contact__lines svg {
    width: 11px;
    height: 11px;
    margin-right: 5px;
    fill: var(--brand-yellow);
    flex: none;
  }
</style>
</head>
<body>
<main class="stage">
  <section class="card card--front">
    <div class="wordmark">Varlonix</div>
    <div class="contact">
      <p class="contact__name">DANIEL HARTWELL</p>
      <p class="contact__title">Managing Director</p>
      <p class="contact__company">VARLONIX, INC.</p>
      <p class="contact__address">18 Fenwick Avenue<br>Halden, Maine 04417</p>
      <ul class="contact__lines">
        <li>
          <svg viewBox="0 0 12 12" aria-hidden="true"><path d="M1 3.5C1 2 2.5 1 6 1s5 1 5 2.5V5H8.5V3.8H3.5V5H1zM3 5.5h6l2 4.5H1z"/></svg>
          044-987 654 321
        </li>
        <li>
          <svg viewBox="0 0 12 12" aria-hidden="true"><path d="M0.5 2.5h11v7h-11z M1.2 3.2 6 7 10.8 3.2" stroke="#fff" stroke-width="0.8"/></svg>
          info@varlonixmail.com
        </li>
        <li>
          <svg viewBox="0 0 12 12" aria-hidden="true"><circle cx="6" cy="6" r="5.5"/><path d="M3 4.5c1-1 2 0 2.5 1s-.5 2 0 3M7 2.5c0 1.5 2 1 2.5 2.5" stroke="#fff" stroke-width="0.8" fill="none"/></svg>
          www.varlonixinc.com
        </li>
      </ul>
    </div>
  </section>
  <section class="card card--back">
    <div class="wordmark">Varlonix</div>
  </section>
</main>
</body>
</html>
```